MossVane Spa, Skincare and Cosmetics website

I need a website for MossVane (putting the glow back into people's skin) which allows viewers to access information about Beauty Spa packaging and facilities as well as online skincare and cosmetic products. Our distinctive difference is that our products are certified organic. We want to target a luxury high income niche market (age 30-50). I want all colours to be "baby colours" preferably background to be "baby metallic pink" (but please don't make the website too immature) with curves as patterns. I want a romantic vintage look.

The website needs to look:
1. elegant (prestige and luxury)
2. bright (baby colours mainly)
3. European curves and signature patterns
4. Can include Pearl related pics (but not a must)

The website pages needs to have:
1. pages ordering skincare/cosmetics
2. shopping cart and payment
3. about us and about our product differences
4. contact us
5. booking for spa treatments and packages

I have attached our logo and also packaging label styles.

Industry/Entity Type

Cosmetics

```html
<!DOCTYPE html>
<html lang="en">
<head>
<meta charset="utf-8">
<title>MossVane Spa, Skincare and Cosmetics</title>
<link rel="stylesheet" href="https://fonts.googleapis.com/css2?family=Open+Sans:wght@300;400;600;700&family=Oswald:wght@300;400&family=Dancing+Script:wght@600&family=Cabin+Sketch&display=swap">
<style>
:root{
  --crimson:#d0124f;
  --crimson-dark:#b8164a;
  --nav-pink:rgba(205,112,150,.85);
  --baby-pink:#f4d2ec;
  --peach:#fcd9bd;
  --peach-edge:#f6c3a0;
  --berry:#a0185c;
  --gold:#f0a020;
  --submit:#d93a3a;
  --footer:#1d1d1d;
  --footer-text:#b9b9b9;
  --footer-accent:#e0507a;
  --taupe:#c9ab98;
  --white:#ffffff;
}
*{box-sizing:border-box;margin:0;padding:0}
html,body{width:853px;height:1200px;overflow:hidden;background:#fff}
body{font-family:"Open Sans",Arial,sans-serif;color:var(--white)}
.page{position:relative;width:853px;height:1200px;overflow:hidden}
.abs{position:absolute}

.hero-photo{left:0;top:0;width:853px;height:1054px;
  background:
    radial-gradient(ellipse 300px 380px at 120px 330px,#3a2a24 0%,rgba(58,42,36,.8) 50%,rgba(58,42,36,0) 100%),
    radial-gradient(ellipse 420px 300px at 520px 560px,#c59878 0%,rgba(197,152,120,0) 100%),
    linear-gradient(180deg,#9fc3dc 0%,#c7a58e 18%,#b88c70 45%,#a8816a 70%,#7f9fc4 88%,#5c86c2 100%)}

.logo-disc{left:114px;top:-23px;width:166px;height:166px;border-radius:50%;background:var(--white);
  box-shadow:0 2px 8px rgba(0,0,0,.25);display:flex;align-items:center;justify-content:center;padding-top:38px}
.brand-name{font-family:"Open Sans",Arial,sans-serif;font-weight:400;color:var(--taupe);font-size:22px;letter-spacing:1px}

.account-links{top:6px;left:575px;font-size:7px;color:#333;word-spacing:6px;letter-spacing:.1px}

.main-nav{left:462px;top:23px;width:281px;height:53px;background:var(--nav-pink);display:flex;align-items:center;font-size:9.5px}
.main-nav a{color:var(--white);text-decoration:none;padding:0 6px;height:100%;display:flex;align-items:center}
.main-nav a.active{background:var(--crimson-dark);padding:0 10px}

.about-title{left:129px;top:192px;font-size:33px;font-weight:300;letter-spacing:.5px}
.about-rule{left:129px;top:239px;width:184px;height:1px;background:var(--gold)}
.about-dot{left:309px;top:235px;width:9px;height:9px;border-radius:50%;background:var(--gold)}
.about-text{left:131px;top:252px;width:200px;font-size:15.5px;line-height:18.6px}

.slider-arrow{top:210px}
.hero-portrait{left:476px;top:105px;width:272px;height:272px;border-radius:50%;
  background:radial-gradient(circle at 40% 45%,#f2d6cf 0%,#d8aea6 45%,#6b4a44 85%,#3a2a28 100%)}

.offer-disc{left:371px;top:198px;width:210px;height:210px;border-radius:50%;background:var(--baby-pink);text-align:center}
.offer-title{position:absolute;left:0;right:0;top:22px;font-family:"Cabin Sketch","Comic Sans MS",cursive;font-size:36px;line-height:34px;color:#4b3b48;letter-spacing:1px}
.offer-rule{position:absolute;left:16px;right:16px;top:100px;height:1px;background:#fff}
.offer-text{position:absolute;left:0;right:0;top:115px;font-size:12.5px;line-height:15.5px;color:var(--berry)}
.book-btn{left:402px;top:377px;width:147px;height:35px;background:var(--crimson);color:var(--white);font-size:15px;display:flex;align-items:center;justify-content:center;box-shadow:0 2px 4px rgba(0,0,0,.25)}

.packages-band{left:316px;top:440px;width:296px;height:32px;background:rgba(250,242,238,.85);border-radius:4px}
.packages-flourish{top:432px;width:90px;height:42px;border-radius:50%;background:rgba(250,242,238,.45)}
.packages-title{left:316px;top:440px;width:296px;height:32px;display:flex;align-items:center;justify-content:center;font-family:"Dancing Script",cursive;font-size:20px;color:var(--crimson)}

.package-card{top:592px;width:200px;height:135px;background:var(--peach);border-radius:4px}
.package-photo{top:500px;width:134px;height:134px;border-radius:50%;border:4px solid var(--peach-edge);
  background:radial-gradient(circle at 50% 40%,#e9c1b6 0%,#a77e86 50%,#3d2c34 100%)}
.product-name{position:absolute;left:72px;top:54px;width:105px;font-size:11px;color:var(--crimson);padding-bottom:3px;border-bottom:1px solid var(--crimson)}
.price-tag{position:absolute;left:8px;top:78px;width:42px;height:42px}
.price-tag .diamond{position:absolute;left:5px;top:5px;width:32px;height:32px;background:var(--crimson);transform:rotate(45deg)}
.price-tag .amount{position:absolute;left:0;top:7px;width:42px;text-align:center;font-size:10px;font-weight:700;line-height:12px;color:var(--white)}
.product-text{position:absolute;left:72px;top:74px;width:124px;font-size:9px;line-height:16px;color:#3a2a2a}

.booking-panel{left:112px;top:752px;width:630px;height:233px;border-radius:4px;
  background:linear-gradient(100deg,#f3a51c 0%,#f0c060 22%,#d8a98a 42%,#c98f78 60%,#e6ddd8 78%,#8fc3e0 100%)}
.booking-title{left:129px;top:786px;font-family:"Oswald","Arial Narrow",sans-serif;font-weight:400;font-size:42px;line-height:54px;text-shadow:0 2px 4px rgba(0,0,0,.45)}
.field{background:rgba(255,255,255,.88);border-radius:3px;color:var(--crimson);font-size:13px;padding:7px 10px}
.submit-btn{left:463px;top:935px;width:218px;height:33px;background:var(--submit);border-radius:2px;font-size:15px;display:flex;align-items:center;justify-content:center}

.site-footer{left:0;top:1054px;width:853px;height:146px;background:linear-gradient(180deg,#242424,var(--footer))}
.footer-brand{left:126px;top:1127px}
.footer-divider{left:263px;top:1083px;height:94px;border-left:1px dotted #8a3a50}
.footer-heading{left:282px;top:1081px;font-size:8.5px;color:var(--footer-accent)}
.footer-text{left:280px;top:1097px;font-size:7.5px;line-height:16.3px;color:var(--footer-text)}
.footer-contact{left:280px;font-size:7.5px;color:var(--footer-text);display:flex;align-items:center;gap:5px}
.footer-links{right:123px;top:1085px;font-size:8px;color:var(--footer-text)}
.social-row{left:623px;top:1113px;display:flex;gap:4px}
.social-row span{width:18px;height:18px;border-radius:50%;background:var(--footer-accent)}
.copyright{right:126px;top:1146px;font-size:7.5px;color:#ddd}
</style>
</head>
<body>
<div class="page">
  <div class="abs hero-photo" role="img" aria-label="Spa photograph of a woman relaxing on a towel during a massage"></div>

  <div class="abs account-links">MY ACCOUNT CHECKOUT SHOP CART (0)</div>
  <nav class="abs main-nav">
    <a class="active">HOME</a><a>ABOUT US</a><a>PRODUCT</a><a>PACKAGES</a><a>CONTACT</a>
  </nav>
  <div class="abs logo-disc"><span class="brand-name">MossVane</span></div>

  <h1 class="abs about-title">ABOUT US</h1>
  <div class="abs about-rule"></div>
  <div class="abs about-dot"></div>
  <p class="abs about-text">Lorem ipsum dolor sit amet, consectetuer fdadpi-scing sed diam nonummy nibh euismod tinciit ut laoreet dor</p>

  <div class="abs hero-portrait" role="img" aria-label="Close-up beauty photograph with fresh makeup"></div>
  <svg class="abs slider-arrow" style="left:354px" width="16" height="52" viewBox="0 0 16 52"><polyline points="15,1 2,26 15,51" fill="none" stroke="#fff" stroke-width="1.2"/></svg>
  <svg class="abs slider-arrow" style="left:752px" width="16" height="52" viewBox="0 0 16 52"><polyline points="1,1 14,26 1,51" fill="none" stroke="#fff" stroke-width="1.2"/></svg>

  <div class="abs offer-disc">
    <div class="offer-title">DAILY<br>OFFER</div>
    <div class="offer-rule"></div>
    <div class="offer-text">lorem ipsum dolor<br>sit is dummy<br>text</div>
  </div>
  <div class="abs book-btn">BOOK NOW</div>

  <div class="abs packages-flourish" style="left:236px" role="img" aria-label="Decorative scroll flourish"></div>
  <div class="abs packages-flourish" style="left:598px" role="img" aria-label="Decorative scroll flourish"></div>
  <div class="abs packages-band"></div>
  <h2 class="abs packages-title">Our Packages</h2>

  <div class="abs package-card" style="left:112px">
    <div class="product-name">PRODUCT NAME</div>
    <div class="price-tag"><div class="diamond"></div><div class="amount">$<br>100.00</div></div>
    <p class="product-text">Lorem ipsum dolor sit amet adipiscing elit, sed diam nonummy nibh euismod</p>
  </div>
  <div class="abs package-card" style="left:327px">
    <div class="product-name">PRODUCT NAME</div>
    <div class="price-tag"><div class="diamond"></div><div class="amount">$<br>100.00</div></div>
    <p class="product-text">Lorem ipsum dolor sit amet adipiscing elit, sed diam nonummy nibh euismod</p>
  </div>
  <div class="abs package-card" style="left:542px">
    <div class="product-name">PRODUCT NAME</div>
    <div class="price-tag"><div class="diamond"></div><div class="amount">$<br>100.00</div></div>
    <p class="product-text">Lorem ipsum dolor sit amet adipiscing elit, sed diam nonummy nibh euismod</p>
  </div>
  <div class="abs package-photo" style="left:145px" role="img" aria-label="Beauty portrait for the first package"></div>
  <div class="abs package-photo" style="left:360px" role="img" aria-label="Beauty portrait for the second package"></div>
  <div class="abs package-photo" style="left:575px" role="img" aria-label="Beauty portrait for the third package"></div>

  <div class="abs booking-panel" role="img" aria-label="Photograph of a woman resting on a towel at the spa"></div>
  <h2 class="abs booking-title">BOOKING FOR<br>SPA TREATMENT<br>AND PACKAGES</h2>
  <div class="abs field" style="left:406px;top:795px;width:155px;height:32px">Name</div>
  <div class="abs field" style="left:567px;top:795px;width:156px;height:32px">Email</div>
  <div class="abs field" style="left:406px;top:834px;width:317px;height:86px">Notes</div>
  <div class="abs submit-btn">SUBMIT</div>

  <footer class="abs site-footer"></footer>
  <div class="abs footer-brand"><span class="brand-name" style="font-size:20px">MossVane</span></div>
  <div class="abs footer-divider"></div>
  <div class="abs footer-heading">ADDRESS</div>
  <p class="abs footer-text">Lorem Ipsum has been the<br>industry's standard dummy text<br>the industry's standard dummy text</p>
  <div class="abs footer-contact" style="top:1148px">
    <svg width="9" height="9" viewBox="0 0 24 24"><path fill="#fff" d="M6.6 10.8a15.1 15.1 0 0 0 6.6 6.6l2.2-2.2c.3-.3.7-.4 1-.2 1.1.4 2.3.6 3.6.6.6 0 1 .4 1 1V20c0 .6-.4 1-1 1A17 17 0 0 1 3 4c0-.6.4-1 1-1h3.5c.6 0 1 .4 1 1 0 1.3.2 2.5.6 3.6.1.3 0 .7-.2 1z"/></svg>1111 1111
  </div>
  <div class="abs footer-contact" style="top:1165px">
    <svg width="9" height="7" viewBox="0 0 18 13"><rect x="0.5" y="0.5" width="17" height="12" fill="#fff"/><polyline points="1,1 9,7 17,1" fill="none" stroke="#1d1d1d" stroke-width="1.4"/></svg>hello@mossvane-spa.com
  </div>
  <div class="abs footer-links">Home • About us • Services • Packages • Contact Us</div>
  <div class="abs social-row"><span></span><span></span><span></span><span></span><span></span></div>
  <div class="abs copyright">Design © 2014. All Rights Reserved</div>
</div>
</body>
</html>
```